Design for an A4 product factsheet

We need a client facing factsheet to explain our products to new and existing clients. There are 10 products, each factsheet needs to have the identical style and layout with the only difference being the copy, we will provide all copy but require a consistent, creative, engaging and 'on brand' layout.

Target market is HR Directors, Compensation & Benefit Managers, Finance Directors and Company Owners

Target Market(s)

Small and Medium sized businesses in the UK with between 50 and 5000 staff

Industry/Entity Type

Product

Other font styles liked:
• Calibri

Requirements
Must have
• An on-brand style consistent with previous designs.
• Use of identical iconography to prior designs for each of our products. These are detailed on the attachments of previous work.
• Immediate impact to grab the attention of a busy professional individual.
• Use of the Vell logo
Nice to have
• Incorporation of our OQR Graphic image.
Should not have
• Any off brand colours

```html
<!DOCTYPE html>
<html lang="en">
<head>
<meta charset="utf-8">
<title>Workplace Pensions – Vell Factsheet</title>
<link rel="stylesheet" href="https://fonts.googleapis.com/css2?family=Carlito:wght@400;700&display=swap">
<style>
  :root {
    --navy: #253a5f;
    --brand-blue: #1a76c0;
    --icon-blue: #1d7fc9;
    --shadow-navy: #1a2a45;
    --cell-grey: #e1e1e6;
    --rule-white: #ffffff;
    --ink: #222222;
    --paper: #ffffff;
  }
  * { box-sizing: border-box; margin: 0; padding: 0; }
  html, body { width: 848px; height: 1200px; overflow: hidden; background: var(--paper); }
  body { font-family: "Carlito", "Calibri", Arial, sans-serif; color: var(--ink); position: relative; }

  .masthead { position: absolute; left: 0; top: 0; width: 848px; height: 192px; background: var(--navy); }
  .product-icon-shadow { position: absolute; left: 58px; top: 110px; width: 122px; height: 102px; }
  .product-icon { position: absolute; left: 48px; top: 100px; width: 112px; height: 112px; background: var(--icon-blue); }
  .page-title { position: absolute; left: 180px; top: 115px; font-size: 38px; font-weight: 700; color: #fff; letter-spacing: 0.2px; }

  .brand-name { position: absolute; left: 690px; top: 84px; width: 100px; text-align: center;
                font-size: 44px; font-weight: 400; line-height: 1; color: #fff; }

  .summary-table { position: absolute; left: 22px; top: 250px; width: 804px; border-collapse: collapse; table-layout: fixed; }
  .summary-table th { background: var(--brand-blue); color: #fff; font-size: 15px; font-weight: 700; text-align: left;
                      height: 48px; padding: 0 0 0 27px; }
  .summary-table td { background: var(--cell-grey); font-size: 13.5px; line-height: 20px; vertical-align: top;
                      height: 130px; padding: 23px 18px 0 27px; }
  .summary-table th + th, .summary-table td + td { border-left: 1px solid var(--rule-white); }
  .summary-table td.two-line { padding-top: 18px; padding-left: 29px; }

  .column { position: absolute; top: 468px; width: 352px; }
  .column-left { left: 52px; }
  .column-right { left: 444px; }
  .section-heading { color: var(--brand-blue); font-size: 16px; font-weight: 700; margin: 0 0 13px; }
  .column p { font-size: 13.6px; line-height: 20px; text-align: justify; margin-bottom: 10px; }
  .column p.tight { margin-bottom: 0; }
  .column .section-heading.spaced { margin-top: 22px; }
</style>
</head>
<body>
  <header class="masthead">
    <svg class="product-icon-shadow" viewBox="0 0 122 102" aria-hidden="true">
      <polygon points="102,92 122,92 102,102" fill="var(--shadow-navy)"/>
    </svg>
    <div class="product-icon" role="img" aria-label="Pension icon: piggy bank held in two hands"></div>
    <h1 class="page-title">Workplace Pensions</h1>
    <span class="brand-name">Vell</span>
  </header>

  <table class="summary-table">
    <colgroup><col style="width:168px"><col style="width:192px"><col style="width:228px"><col style="width:216px"></colgroup>
    <thead>
      <tr><th>Benefit</th><th>Employer Tax</th><th>Employee Tax</th><th>Cost to Employer</th></tr>
    </thead>
    <tbody>
      <tr>
        <td>Workplace Pension</td>
        <td>Corporation Tax relief</td>
        <td class="two-line">Income Tax relief at highest rate<br>Tax efficient growth within pension fund</td>
        <td class="two-line">Current minimum is 1% Employer contribution based on Qualifying Earnings (£5,824 - £43,000)</td>
      </tr>
    </tbody>
  </table>

  <section class="column column-left">
    <h2 class="section-heading">What it a Workplace Pension?</h2>
    <p>A Workplace pension is a pension scheme offered by an employer, into which the employer (and usually the employee) makes a contribution.</p>
    <p class="tight">Since the introduction of Auto-Enrolment in 2012, all companies will have to offer a Workplace Pension by the end of 2019, and make contributions into it.</p>
    <p>A Workplace Pension can be offered through a variety of pension providers in the UK.</p>
    <h2 class="section-heading spaced">How does it work?</h2>
    <p>There are two main types of Workplace Pension.</p>
    <p>The first is a Defined Benefit (DB) scheme, more commonly known as a final salary pension. There aren’t many of these left in the private sector, but they are common in the public sector. Under a DB scheme, you are credited with a fraction of your salary for each year you work, e.g. 1/60th. So, after 40 years in the scheme, you could retire on 40/60ths (2/3rds) of your salary.</p>
    <p>The second, and much more common, type of Workplace Pension is a Defined Contribution (DC) or money purchase pension scheme. These pensions are set up as a series of individual pension policies held under the employer’s group pension arrangement. Each employee has their own individual pension “pot” and their money is managed by the pension provider in accordance with their wishes. DC pensions are not guaranteed in the same way as DB pensions, as the final “pot” at retirement depends on the contributions made and the investment growth over the term of the pension.</p>
  </section>

  <section class="column column-right">
    <h2 class="section-heading">Why is it valuable?</h2>
    <p>A Workplace Pension is a tax-efficient way for employees to save for retirement. The State Pension is £155.65 per week (2016/17) and most people agree that the State Pension alone won’t be enough for them to live on in their later years. In addition, as the State Pension Age has been pushed further and further up, many people want to look at being able to fund their retirement without having to wait until age 68. Workplace pensions can currently be accessed from age 55.</p>
    <p>Pension contributions receive tax relief at an individual’s highest rate, so that’s either 20%, 40% or 45%. In addition, because employers now have to pay into a Workplace Pension, that makes it even more attractive for employees.</p>
    <p>For employers, it is a tax-efficient way to reward employees, as pension contributions can be offset against their Corporation tax bill and, unlike salary, is not subject to Employer’s National Insurance.</p>
    <h2 class="section-heading spaced">What does it cost?</h2>
    <p>Employers have to pay at least 1% of “qualifying earnings” (earnings between £5,824 and £43,000) into a Workplace Pension, and most companies ask their employees to make a contribution as well. Any amount above this minimum should be seen as a definite benefit to the employees.</p>
  </section>
</body>
</html>
```